Design of Stationery (Business Card, Letterhead and Envelope) for Investment Company
Kestrelmoor Capital Associates Limited
Design of Stationery (Business Card, Letterhead and Envelope) for Investment Company - Financial Services
Creative Brief
Simple
Tunde A. Ibekwe
Director
7C, Dunmore Crescent, Osapa Garden Estate, Lekki Peninsula, Lagos
tunde@kestrelmoorng.example
www.kestrelmoorng.example
RC 458290
The back of the business card should have the logo of the company on navy blue background - please see the logo uploaded. Below the logo should be the words: "INVESTMENTS. ADVICE. VALUE CREATION".

```html
<!DOCTYPE html>
<html lang="en">
<head>
<meta charset="UTF-8">
<title>Kestrelmoor Capital Associates – Business Card</title>
<link rel="stylesheet" href="https://fonts.googleapis.com/css2?family=Open+Sans:wght@400;600&display=swap">
<style>
  :root {
    --backdrop: #e6e8eb;
    --card-top: #f7f8f9;
    --card-bottom: #e4e7ea;
    --navy: #2c3e63;
    --navy-deep: #1f2e4d;
    --silver-light: #f1f2f4;
    --silver-dark: #c9ced5;
    --white: #ffffff;
    --text-muted: #4a5671;
  }
  * { margin: 0; padding: 0; box-sizing: border-box; }
  html, body {
    width: 1200px;
    height: 770px;
    overflow: hidden;
    background: var(--backdrop);
    font-family: "Open Sans", Arial, sans-serif;
  }
  .business-card {
    position: absolute;
    left: 120px;
    top: 106px;
    width: 960px;
    height: 557px;
    border-radius: 22px;
    background: linear-gradient(180deg, var(--card-top) 0%, var(--card-bottom) 100%);
    box-shadow: 0 18px 40px rgba(31, 46, 77, 0.18);
    overflow: hidden;
  }
  .brand {
    position: absolute;
    left: 0;
    top: 92px;
    width: 100%;
    display: flex;
    justify-content: center;
    align-items: center;
    gap: 22px;
  }
  .brand-square {
    width: 72px;
    height: 72px;
    border-radius: 5px;
    background: var(--navy);
    flex: none;
  }
  .brand-name {
    font-family: "Open Sans", Arial, sans-serif;
    font-size: 40px;
    font-weight: 600;
    color: var(--navy);
    white-space: nowrap;
  }
  .info-band {
    position: absolute;
    left: 0;
    top: 252px;
    width: 100%;
    height: 228px;
    background: linear-gradient(180deg, var(--navy) 0%, var(--navy-deep) 100%);
  }
  .band-notch {
    position: absolute;
    left: 210px;
    top: -1px;
    width: 0;
    height: 0;
    border-left: 16px solid transparent;
    border-right: 16px solid transparent;
    border-top: 18px solid var(--card-top);
  }
  .person {
    position: absolute;
    left: 40px;
    width: 380px;
    top: 84px;
    text-align: center;
    color: var(--white);
  }
  .person-name {
    font-size: 28px;
    font-weight: 600;
    letter-spacing: 1px;
    text-transform: uppercase;
  }
  .person-title {
    font-size: 22px;
    margin-top: 4px;
  }
  .band-divider {
    position: absolute;
    left: 452px;
    top: 30px;
    width: 2px;
    height: 168px;
    background: rgba(255, 255, 255, 0.75);
  }
  .contact-list {
    position: absolute;
    left: 488px;
    top: 34px;
    list-style: none;
    color: var(--white);
    font-size: 19px;
  }
  .contact-list li {
    display: flex;
    align-items: center;
    gap: 14px;
    height: 40px;
  }
  .contact-icon {
    width: 26px;
    height: 26px;
    flex: none;
  }
  .web-strip {
    position: absolute;
    left: 0;
    top: 480px;
    width: 100%;
    height: 77px;
    background: linear-gradient(180deg, var(--silver-light) 0%, var(--silver-dark) 100%);
    text-align: center;
    padding-top: 14px;
    font-size: 21px;
    font-weight: 600;
    letter-spacing: 2px;
    color: var(--text-muted);
  }
</style>
</head>
<body>
  <main class="business-card">
    <div class="brand">
      <div class="brand-square"></div>
      <p class="brand-name">Kestrelmoor Capital Associates</p>
    </div>

    <section class="info-band">
      <div class="band-notch"></div>

      <div class="person">
        <p class="person-name">Tunde A. Ibekwe</p>
        <p class="person-title">Director</p>
      </div>

      <div class="band-divider"></div>

      <ul class="contact-list">
        <li>
          <svg class="contact-icon" viewBox="0 0 26 26" aria-hidden="true">
            <circle cx="13" cy="13" r="13" fill="#ffffff"/>
            <path d="M9 7.5c.6-.4 1.3-.2 1.6.4l1 2c.3.5.1 1.1-.3 1.4l-.8.6c.6 1.4 1.6 2.4 3 3l.6-.8c.3-.4.9-.6 1.4-.3l2 1c.6.3.8 1 .4 1.6l-.6.9c-.5.7-1.4 1-2.2.7-3.2-1.1-5.6-3.5-6.7-6.7-.3-.8 0-1.7.7-2.2z" fill="#2c3e63"/>
          </svg>
          <span>014 528 3071</span>
        </li>
        <li>
          <svg class="contact-icon" viewBox="0 0 26 26" aria-hidden="true">
            <circle cx="13" cy="13" r="13" fill="#ffffff"/>
            <path d="M9 7.5c.6-.4 1.3-.2 1.6.4l1 2c.3.5.1 1.1-.3 1.4l-.8.6c.6 1.4 1.6 2.4 3 3l.6-.8c.3-.4.9-.6 1.4-.3l2 1c.6.3.8 1 .4 1.6l-.6.9c-.5.7-1.4 1-2.2.7-3.2-1.1-5.6-3.5-6.7-6.7-.3-.8 0-1.7.7-2.2z" fill="#2c3e63"/>
          </svg>
          <span>014 528 3072</span>
        </li>
        <li>
          <svg class="contact-icon" viewBox="0 0 26 26" aria-hidden="true">
            <circle cx="13" cy="13" r="13" fill="#ffffff"/>
            <rect x="6.5" y="8.5" width="13" height="9" rx="1" fill="none" stroke="#2c3e63" stroke-width="1.6"/>
            <path d="M7 9.2l6 4.6 6-4.6" fill="none" stroke="#2c3e63" stroke-width="1.6"/>
          </svg>
          <span>tunde@kestrelmoorng.example</span>
        </li>
        <li>
          <svg class="contact-icon" viewBox="0 0 26 26" aria-hidden="true">
            <circle cx="13" cy="13" r="13" fill="#ffffff"/>
            <path d="M13 5.5c-2.8 0-5 2.2-5 5 0 3.6 5 9.5 5 9.5s5-5.9 5-9.5c0-2.8-2.2-5-5-5z" fill="#2c3e63"/>
            <circle cx="13" cy="10.5" r="1.9" fill="#ffffff"/>
          </svg>
          <span>7C Dunmore Crescent, Lekki, Lagos</span>
        </li>
      </ul>
    </section>

    <footer class="web-strip">www.kestrelmoorng.example</footer>
  </main>
</body>
</html>
```